WordPress Design - dental products

We need a Wordpress theme for a company based in Mexico, USA and Europe. We sell orthodontic products for dental industry. We are very compromised with our customers and all our products are the better option in the market. The Quality and image are really important for us.

The idea is to have a Wordpress Website that we can manage, and our customers can get info from us. Our corporate image is based in innovation, quality and customer service.

the general idea is to have a wordpress site to manage all the info and the store is in a different system, so that we need is the wordpress site desing for the frontend. 

We will need more designs so in the future for our website, so the winner will help us for many projects.

So we hope the best design.
Updates

Hi, this "wordpress site" will be used as a homepage, the eCommerce is independent. So the design is related to corporate site. Thank you

Target Market(s)

Target: dental and orthodontic industry, academy and general customers. Private an public organizations related to medical and dental industry.
Investigators and press

Industry/Entity Type

Dental

Requirements
Must have
• Must Have Priorities:
• - Respect the logo (included)
• - Respect colors (actual website)
• - Modern style and innovated website
Nice to have
• Be funcionality, simply and easy to use, think about user interfaze (UI)
Should not have
• The design should not use old-style, serif fonts like Times New Roman. Not use cartoons, flash animations, free icons. Don't modify the logo.

```html
<!DOCTYPE html>
<html lang="en">
<head>
<meta charset="utf-8">
<title>Orto-Lumen – Orthodontic Products</title>
<link href="https://fonts.googleapis.com/css2?family=Ubuntu:wght@400;500&family=Noto+Sans:wght@400;700&display=swap" rel="stylesheet">
<style>
:root{
  --topbar:#8c0a1c;
  --header:#1f1e1e;
  --red:#b1102a;
  --red-dark:#7d0719;
  --red-light:#c81c36;
  --cream:#efe8d6;
  --cream-bg:#e6dcc2;
  --tan:#d0b992;
  --tan-text:#5e4a2e;
  --body-text:#5a5247;
  --footer:#1e1d1d;
  --footer-text:#a9a49b;
  --footer-head:#e8d8b0;
  --white:#ffffff;
}
*{margin:0;padding:0;box-sizing:border-box}
html,body{width:1108px;height:1200px;overflow:hidden}
body{position:relative;background:var(--cream-bg);font-family:"Noto Sans",sans-serif;color:var(--body-text)}
.abs{position:absolute}
.topbar{left:0;top:0;width:1108px;height:11px;background:var(--topbar)}
.flags{right:38px;top:2px;display:flex;gap:5px}
.flags span{width:13px;height:8px;background:#ddd;display:block}
.header{left:0;top:11px;width:1108px;height:92px;background:var(--header);border-bottom:1px solid #000}
.brand{left:113px;top:6px;display:flex;align-items:center;gap:10px}
.brand-mark{width:58px;height:83px;border:2px solid #c9b48a;display:block}
.brand-name{font-family:"Ubuntu",sans-serif;font-weight:500;font-size:30px;color:var(--white);letter-spacing:.5px}
.contact-line{right:111px;top:17px;font-family:"Ubuntu",sans-serif;font-size:16px;color:#8f8a84;display:flex;gap:16px}
.contact-line .sep{color:#555}
.search{left:680px;top:50px;display:flex;gap:7px}
.search-input{width:241px;height:24px;border-radius:4px;background:#fff;border:2px solid #d8c79f;font-size:13px;color:#c4bba9;padding:2px 10px;font-family:"Ubuntu",sans-serif}
.search-btn{width:67px;height:24px;border-radius:4px;background:#f3ecd9;border:2px solid #d8c79f;font-family:"Ubuntu",sans-serif;font-size:14px;color:#333;text-align:center;line-height:20px}
.nav{left:0;top:103px;width:1108px;height:45px;background:linear-gradient(var(--red-light),var(--red) 60%,#9c0c23);border-top:1px solid #e0354e;border-bottom:1px solid #e0354e}
.nav ul{list-style:none;position:absolute;left:103px;top:0;display:flex;height:44px}
.nav li{font-family:"Ubuntu",sans-serif;font-size:16px;color:#f6e6cf;line-height:44px;padding:0 14px;border-left:1px solid #7a0718}
.nav li:first-child{border-left:none}
.hero{left:0;top:148px;width:1108px;height:321px;background:linear-gradient(var(--red),#a30c27 60%,#86061b)}
.slide{left:192px;top:34px;width:725px;height:256px;border:2px solid #f0c6a4;border-radius:4px;background:linear-gradient(90deg,#e9a88f 0%,#f3c2a2 35%,#e39a6c 70%,#d9895a 100%);overflow:hidden}
.slide-photo{position:absolute;left:0;top:0;width:390px;height:252px;background:linear-gradient(135deg,#b9695a,#f2ddd0 50%,#c07c6c)}
.slide-copy{position:absolute;left:406px;top:62px;color:#fff;font-family:"Noto Sans",sans-serif;font-weight:700}
.slide-copy .q{position:absolute;font-size:48px;line-height:1;color:#9b5a3a;font-family:Georgia,serif}
.slide-copy h2{font-size:34px;line-height:1}
.slide-copy h3{font-size:21px;margin-top:4px}
.slide-copy p{font-size:15px;line-height:18px;margin-top:14px}
.arrow{top:120px}
.content{left:0;top:469px;width:1108px;height:512px;background:linear-gradient(#f6f0e1,var(--cream-bg) 40px)}
.panel-head{height:35px;background:linear-gradient(#d9c4a0,var(--tan));border-radius:3px 3px 0 0;font-weight:700;font-size:16px;color:var(--tan-text);padding:7px 11px;text-shadow:0 1px 0 #e9dcc0}
.panel-body{background:var(--cream);border-top:2px solid #f7f2e5}
.sidebar{left:112px;top:24px;width:159px}
.sidebar .panel-body{height:432px;padding:12px 8px}
.product-list{list-style:none}
.product-list li{font-size:12px;line-height:21px;padding-left:4px;border-bottom:1px dotted #c9b48f;height:22.2px;color:#4c443a}
.product-list li:last-child{border-bottom:none}
.welcome{left:279px;top:24px;width:717px}
.welcome .panel-body{height:251px;position:relative;font-size:12px;line-height:16.6px;letter-spacing:.1px}
.welcome-photo{position:absolute;left:12px;top:15px;width:182px;height:158px;border:3px solid #fff;background:linear-gradient(160deg,#e7c6ae,#a9795e 60%,#d7b19a)}
.welcome-text{position:absolute;left:206px;top:12px;width:499px;text-align:justify}
.welcome-text p+p{margin-top:16px}
.welcome-foot{position:absolute;left:11px;top:195px;width:695px}
.featured{left:279px;top:319px;width:717px}
.featured .panel-body{height:138px;position:relative}
.thumb{position:absolute;top:12px;width:97px;text-align:center;font-size:11px;color:#4c443a}
.thumb-box{width:97px;height:98px;background:#fff;border:2px solid #e8dcc3;margin-bottom:8px}
.footer{left:0;top:981px;width:1108px;height:219px;background:var(--footer);color:var(--footer-text);font-size:11px;line-height:14.8px;letter-spacing:.3px}
.footer h4{font-size:16px;color:var(--footer-head);font-weight:700;margin-bottom:14px}
.col-divider{width:1px;background:#3a3838}
.footer ul{list-style:none}
.news li{margin-bottom:14px;padding-left:9px;position:relative}
.news li:before{content:"•";position:absolute;left:0}
.footer a{color:var(--footer-text)}
.join{left:803px;top:34px;width:120px}
.join h4{margin-left:19px;margin-bottom:4px}
.social{margin-left:8px;width:113px;height:33px;border-radius:0 16px 16px 0;background:#151414;display:flex;gap:16px;padding:6px 10px}
.social span{width:18px;height:18px;background:#c9c4bb;border-radius:2px;display:block}
</style>
</head>
<body>
<div class="abs topbar">
  <div class="abs flags"><span style="background:#d52b1e"></span><span style="background:#4a6fb5"></span><span style="background:#2d8a4a"></span><span style="background:#3b4a8f"></span><span style="background:#e0c21a"></span></div>
</div>

<header class="abs header">
  <div class="abs brand"><span class="brand-mark"></span><span class="brand-name">Orto-Lumen</span></div>
  <div class="abs contact-line"><span>+52 555 010 2040</span><span class="sep">|</span><span>info@ortolumen.com</span></div>
  <div class="abs search"><div class="search-input">Product Search</div><div class="search-btn">Search</div></div>
</header>

<nav class="abs nav">
  <ul>
    <li>Home</li><li>About Us</li><li>Products</li><li>Online Catalogue</li><li>Best Sellers</li><li>News / Events</li><li>Customer Care</li><li>Contact</li>
  </ul>
</nav>

<section class="abs hero">
  <svg class="abs arrow" style="left:112px" width="56" height="62" viewBox="0 0 56 62"><path d="M54 0 L0 31 L54 62 L54 54 L16 31 L54 8 Z" fill="#8a0a20"/><path d="M54 8 L16 31 L54 54" fill="none" stroke="#c8243d" stroke-width="2"/></svg>
  <div class="abs slide">
    <div class="slide-photo" role="img" aria-label="Close-up photo of a smile with a dental mirror"></div>
    <div class="slide-copy">
      <span class="q" style="left:-8px;top:-34px">“</span>
      <h2>Lorem Ipsum</h2>
      <h3>is simply dummy text</h3>
      <p>It was popularised in the 1960s<br>with the release of Typoline sheets<br>containing Lorem Ipsum passages</p>
      <span class="q" style="left:292px;top:116px">”</span>
    </div>
  </div>
  <svg class="abs arrow" style="left:942px" width="56" height="62" viewBox="0 0 56 62"><path d="M2 0 L56 31 L2 62 L2 54 L40 31 L2 8 Z" fill="#8a0a20"/><path d="M2 8 L40 31 L2 54" fill="none" stroke="#c8243d" stroke-width="2"/></svg>
</section>

<main class="abs content">
  <aside class="abs sidebar">
    <div class="panel-head">Product List</div>
    <div class="panel-body">
      <ul class="product-list">
        <li>Acrylics</li><li>Banding</li><li>Bracer Products</li><li>Bonding</li><li>Brackets</li><li>Brushes &amp; Accessories</li><li>Disposables</li><li>Elastomerics</li><li>Equipment</li><li>Vexalign</li><li>Facebows</li><li>Hand Instruments</li><li>Handpieces</li><li>Headgear</li><li>Impressions</li><li>Infection Control</li><li>Instruments</li><li>Interproximal Stripping</li><li>Models</li>
      </ul>
    </div>
  </aside>

  <section class="abs welcome">
    <div class="panel-head">Welcome to Orto-Lumen</div>
    <div class="panel-body">
      <div class="welcome-photo" role="img" aria-label="Photo of two smiling young people"></div>
      <div class="welcome-text">
        <p>Lorem Ipsum is simply dummy text of the printing and typesetting industry. Lorem Ipsum has been the industry's standard dummy text ever since the 1500s, when an unknown printer took a galley of type and scrambled it to make a type specimen book. It has survived not only five centuries, but also the leap into electronic typesetting, remaining essentially unchanged.</p>
        <p>It was popularised in the 1960s with the release of Typoline sheets containing Lorem Ipsum passages, and more recently with desktop publishing software like Quill PageForm including versions of Lorem Ipsum.</p>
      </div>
      <p class="welcome-foot">Lorem Ipsum is simply dummy text of the printing and typesetting industry. Lorem Ipsum has been the industry's standard dummy text ever since the 1500s, when an unknown printer took a galley of type and scrambled it to make a type specimen book.</p>
    </div>
  </section>

  <section class="abs featured">
    <div class="panel-head">Featured Products</div>
    <div class="panel-body">
      <div class="thumb" style="left:11px"><div class="thumb-box"></div>Headgear</div>
      <div class="thumb" style="left:131px"><div class="thumb-box"></div>Product Name</div>
      <div class="thumb" style="left:251px"><div class="thumb-box"></div>Dummy Name</div>
      <div class="thumb" style="left:370px"><div class="thumb-box"></div>Name Keyword</div>
      <div class="thumb" style="left:490px"><div class="thumb-box"></div>Bastomerics</div>
      <div class="thumb" style="left:610px"><div class="thumb-box"></div>Olastomerics</div>
    </div>
  </section>
</main>

<footer class="abs footer">
  <div class="abs" style="left:111px;top:16px">
    <h4>Sitemap</h4>
    <ul><li>Home</li><li>Product List</li><li>About Us</li><li>News / Events</li><li>Best Sellers</li><li>Customer Support</li><li>Branches</li><li>Contact Us</li><li>Terms &amp; Conditions</li></ul>
  </div>
  <div class="abs col-divider" style="left:244px;top:20px;height:176px"></div>
  <div class="abs news" style="left:272px;top:16px;width:292px">
    <h4>News / Events</h4>
    <ul>
      <li>Phasellus nec lectus at augue semper ullamcor per lectus at augue.</li>
      <li>Donec a eros et nulla sollicitudin imperdiet quis.</li>
      <li>Nam eget tortor leo, non volutpat erat.</li>
      <li>Aenean quis augue vitae nisi dignissim conse quat lectus at augue.</li>
    </ul>
  </div>
  <div class="abs col-divider" style="left:570px;top:20px;height:176px"></div>
  <div class="abs" style="left:605px;top:16px;width:180px">
    <h4>Contact Us</h4>
    <p>Orto-Lumen<br>dummy text of the printing<br>and typesetting industry.<br>ph: +5255501020<br>email: <a href="#">info@ortolumen.com</a></p>
    <h4 style="margin-top:13px;margin-bottom:8px">Branches</h4>
    <p>» Mexico &nbsp; » USA &nbsp; » Europe</p>
  </div>
  <div class="abs col-divider" style="left:803px;top:24px;height:130px"></div>
  <div class="abs join">
    <h4>Join us</h4>
    <div class="social"><span></span><span></span><span></span></div>
    <p style="margin-left:8px;margin-top:12px;font-size:10.5px;line-height:13px;width:200px">Copyright © 2010 ortolumen.<br>All Rights Reserved.</p>
  </div>
</footer>
</body>
</html>
```